Business Card Design for Vantor Gear

We want to have a business card design for our company.
Company website: www.vantorgear-example.com.au
We looking for something cool, funky, and impressive, yet elegant.
Below are the contents that should be displayed on the card:
Front:
Name: Mark Dellow
Title: Sales & Purchasing
Company Name: Vantor Gear Pty Ltd
Phone: 02 5550 1473
Mobile: 0400 555 019
Email: mark@vantorgear-example.com.au
Website: www.vantorgear-example.com.au
Address: 17 Brackley St
Harwell, NSW 2199
Back:
We buy sell new used Norvex and network equipment
• Huge Savings - save up to 95% off list prices
• Highest Reliability
• Comprehensive Warranty
• Fast delivery
• Large range of hardware in stock
Our logo can be downloaded at: www.vantorgear-example.com.au/logo.zip

```html
<!DOCTYPE html>
<html lang="en">
<head>
<meta charset="utf-8">
<title>Vantor Gear — Business Card</title>
<link rel="stylesheet" href="https://fonts.googleapis.com/css2?family=PT+Sans:wght@700&family=Tinos:wght@400&display=swap">
<style>
  :root {
    --page: #d9d9d9;
    --card: #050505;
    --card-edge: #1a1a1a;
    --brand-blue: #2f8fe0;
    --text-blue: #3a8fd8;
    --text-white: #f2f2f2;
    --text-grey: #9a9a9a;
    --mark-orange: #f07a1c;
  }
  * { box-sizing: border-box; margin: 0; padding: 0; }
  html, body { width: 1200px; height: 960px; overflow: hidden; }
  body {
    background: var(--page);
    display: flex;
    flex-direction: column;
    align-items: center;
    justify-content: center;
    gap: 40px;
    font-family: "Tinos", "Times New Roman", serif;
  }
  .card {
    position: relative;
    width: 760px;
    height: 434px;
    background: var(--card);
    border: 1px solid var(--card-edge);
    box-shadow: 0 10px 28px rgba(0,0,0,.35);
    overflow: hidden;
  }
  .brand {
    position: absolute;
    display: flex;
    align-items: center;
    gap: 22px;
  }
  .brand-dot {
    width: 96px; height: 96px;
    border-radius: 50%;
    background: var(--mark-orange);
    flex: none;
  }
  .brand-name {
    font-family: "PT Sans", Arial, sans-serif;
    font-weight: 700;
    color: var(--brand-blue);
    line-height: 1;
  }
  .brand-tagline {
    font-family: "PT Sans", Arial, sans-serif;
    font-weight: 700;
    color: var(--text-white);
    letter-spacing: .38em;
    text-transform: uppercase;
    margin-top: 10px;
  }

  /* Front */
  .card-front .brand { left: 34px; top: 34px; }
  .card-front .brand-name { font-size: 66px; }
  .card-front .brand-tagline { font-size: 17px; }
  .identity {
    position: absolute;
    left: 150px; top: 200px;
    display: flex;
    align-items: center;
    gap: 12px;
    color: var(--text-blue);
  }
  .person-name { font-size: 34px; text-transform: uppercase; }
  .identity-role {
    border-left: 2px solid var(--text-blue);
    padding-left: 10px;
    font-size: 21px;
    line-height: 1.15;
  }
  .address {
    position: absolute;
    left: 620px; top: 262px;
    color: var(--text-grey);
    font-size: 17px;
    font-style: normal;
    line-height: 1.2;
  }
  .contacts {
    position: absolute;
    left: 40px; bottom: 40px;
    display: grid;
    grid-template-columns: auto auto;
    column-gap: 60px;
    row-gap: 12px;
    color: var(--text-blue);
    font-size: 20px;
  }
  .contact { display: flex; align-items: center; gap: 12px; }
  .contact svg { width: 22px; height: 22px; flex: none; fill: var(--text-white); }

  /* Back */
  .card-back .brand { left: 40px; top: 40px; }
  .card-back .brand-dot { width: 90px; height: 90px; }
  .card-back .brand-name { font-size: 62px; }
  .card-back .brand-tagline { font-size: 16px; }
  .pitch {
    position: absolute;
    left: 40px; right: 40px; top: 190px;
    color: var(--text-white);
  }
  .pitch-lead { font-size: 25px; margin-bottom: 18px; }
  .benefits {
    list-style: none;
    display: grid;
    grid-template-columns: 1.35fr 1fr;
    row-gap: 14px;
    font-size: 23px;
  }
  .benefits li::before { content: "• "; }
  .benefits .wide { grid-column: 1 / -1; }
</style>
</head>
<body>

  <section class="card card-front" aria-label="Business card front">
    <div class="brand">
      <span class="brand-dot"></span>
      <div>
        <div class="brand-name">Vantor Gear</div>
        <div class="brand-tagline">Networking Equipment</div>
      </div>
    </div>

    <div class="identity">
      <span class="person-name">Mark Dellow</span>
      <span class="identity-role">Vantor Gear Pty Ltd<br>Sales &amp; Purchasing</span>
    </div>

    <address class="address">17 Brackley St<br>Harwell,<br>NSW 2199</address>

    <div class="contacts">
      <div class="contact">
        <svg viewBox="0 0 24 24" aria-hidden="true"><path d="M3 8c0-2 4-4 9-4s9 2 9 4v2h-5V8H8v2H3zM6 11h12l2 9H4z"/></svg>
        02 5550 1473
      </div>
      <div class="contact">
        <svg viewBox="0 0 24 24" aria-hidden="true"><path d="M12 3a9 9 0 1 0 5 16.5l-1-1.6A7 7 0 1 1 19 12v1a1.5 1.5 0 0 1-3 0V8h-2v.8A4 4 0 1 0 15 16a3.5 3.5 0 0 0 6-3v-1a9 9 0 0 0-9-9zm0 11a2 2 0 1 1 0-4 2 2 0 0 1 0 4z"/></svg>
        mark@vantorgear-example.com.au
      </div>
      <div class="contact">
        <svg viewBox="0 0 24 24" aria-hidden="true"><path d="M7 2h10a1 1 0 0 1 1 1v18a1 1 0 0 1-1 1H7a1 1 0 0 1-1-1V3a1 1 0 0 1 1-1zm1 3v12h8V5zm4 13.5a1 1 0 1 0 0 2 1 1 0 0 0 0-2z"/></svg>
        0400 555 019
      </div>
      <div class="contact">
        <svg viewBox="0 0 24 24" aria-hidden="true"><path d="M12 2a10 10 0 1 0 0 20 10 10 0 0 0 0-20zm6.9 9h-3a15 15 0 0 0-1.4-6A8 8 0 0 1 18.9 11zM12 4.1A13 13 0 0 1 13.9 11h-3.8A13 13 0 0 1 12 4.1zM9.5 5a15 15 0 0 0-1.4 6h-3A8 8 0 0 1 9.5 5zm-4.4 8h3a15 15 0 0 0 1.4 6A8 8 0 0 1 5.1 13zm6.9 6.9A13 13 0 0 1 10.1 13h3.8A13 13 0 0 1 12 19.9zm2.5-.9a15 15 0 0 0 1.4-6h3a8 8 0 0 1-4.4 6z"/></svg>
        www.vantorgear-example.com.au
      </div>
    </div>
  </section>

  <section class="card card-back" aria-label="Business card back">
    <div class="brand">
      <span class="brand-dot"></span>
      <div>
        <div class="brand-name">Vantor Gear</div>
        <div class="brand-tagline">Networking Equipment</div>
      </div>
    </div>

    <div class="pitch">
      <p class="pitch-lead">We buy sell new used Norvex and network equipment</p>
      <ul class="benefits">
        <li class="wide">Huge Savings - save up to 95% off list prices</li>
        <li>Comprehensive Warranty</li>
        <li>Highest Reliability</li>
        <li>Large range of hardware in stock</li>
        <li>Fast delivery</li>
      </ul>
    </div>
  </section>

</body>
</html>
```